Web-page design

We need a initial web design for our page kavilora.com.au (which is not yet set up).
We provide consulting services for all kinds of problems in and between organisations.
Main focus is on conflict resolution but we also support companies on improving their operational performance.
We want to have the following page structure (and part of the project is to design the 8 pages):
- Home
- Services (we offer 3 main service areas - one per page)
- Case studies (one per page)
- Engaging us (our process)
- About Conflict & low performance
- Conflict resolution App
- About
- Contact (Email form)
- Our logo should be on each page.
The start page should include the following information:
- Twitter / Linkedin / facebook/ google + Links
- Telephone / Email or in general contact details
- News
- A quite prominent picture box with 3 alternating pics - each representing one of our service areas
- Link to our App
- Testimonials
It would be nice if the service pages would have an image header. Links to the information section (about conflict & low performance; and the app page) would be nice as well.
We like the following joomla designs: www.quorbixlane.com/itempreview/153
No need to copy it, it should just give you an idea.
We like the layout here with the picture and space for the case studies on the left. Somewhere beneath should be the 3 service areas with a picture each.
In terms of colors: our logo colours are Blue (RBG 8;44;80) and Orange (RGB 231;120;23). The orange could be used to emphasise certain things, however there should not be too much color.
Budget for images available, so please use placeholders or ask us for specific photos/images, if you need them for your design.
Updates
Hi, one more thing that we would like to have is the case studies not hidden behind a link "case studies" - we would like to have them individually linked prominent on the first page. There will be about 6-8 of them. Thats what we liked on the joomla template (the links left from the picture).
Hi, thanks very much for all the great proposals.
We are currently going through the selection process and will post our decision early next week.
Thanks again!
Liesel
Target Market(s)
- target customers are all different kinds of businesses and organisations (all industries, government, non-for-profit, ...) experiencing conflict and tension - be it with internal staff, amongst managers or board members, dysfunctional teams, between organizations or customers and organizations... examples could be bullying allegations, governmental negotiations with unions, disputes within organizations etc.
- also we will offer performance improvement services for organizations
- we will offer mediation, facilitation, negotiation, performance improvement services, conflict coaching, conflict management, change management services
- if comparable to anything - then to a law firm in terms of dealing with conflicts but its much less adversarial and much more about the people and their interests rather than about laws
- basically it's all kind of things you can do in order to solve disputes without involving lawyers and a court - so it's much cheaper and target is to find a solution all parties can live with rather than having a judge deciding about who wins and who looses
- performance management is more about analysing reasons for a lack of performance and setting up continous improvement systems, supporting change management, facilitating improvement workshops or strategic meetings, ...
Industry/Entity Type
Consulting
Look and feel

```html
<!DOCTYPE html>
<html lang="en">
<head>
<meta charset="utf-8">
<title>Kavilora Partners – Conflict Resolution &amp; Performance</title>
<link href="https://fonts.googleapis.com/css2?family=Open+Sans:ital,wght@0,300;0,400;0,600;0,700;1,300;1,400&display=swap" rel="stylesheet">
<style>
:root{
  --navy:#082c50;
  --orange:#e77817;
  --ink:#2a2a2a;
  --text:#6a6a6a;
  --muted:#9a9a9a;
  --rule:#dcdcdc;
  --page:#f3f3f3;
  --panel:#ffffff;
  --dark:#2b2b2b;
}
*{box-sizing:border-box;margin:0;padding:0}
html,body{width:794px;height:1200px;overflow:hidden}
body{background:var(--page);font-family:"Open Sans",Arial,sans-serif;color:var(--text);position:relative}
.abs{position:absolute}
a{color:inherit;text-decoration:none}

.main-nav{left:198px;top:14px;width:389px;display:flex;justify-content:space-between;font-size:5.6px;letter-spacing:.2px;color:var(--muted);text-transform:uppercase}
.main-nav .current{color:var(--ink);font-weight:700;position:relative}
.main-nav .current::after{content:"";position:absolute;left:50%;top:9px;margin-left:-2px;border:2px solid transparent;border-top-color:var(--ink)}

.brand{left:208px;top:49px;display:flex;align-items:center;gap:14px}
.brand-mark{width:34px;height:34px;border:3px solid var(--orange)}
.brand-name{font-size:20px;font-weight:400;color:var(--navy);letter-spacing:.4px;line-height:1;white-space:nowrap}
.brand-url{left:258px;top:80px;font-size:7.5px;letter-spacing:6.6px;font-weight:600;color:var(--navy);white-space:nowrap}
.social{left:527px;top:61px;display:flex;gap:3px}
.social span{width:13px;height:13px;border-radius:50%;background:#cfcfcf}
.brand-rule{left:198px;top:95px;width:389px;height:3px;background:var(--orange)}

.hero{left:198px;top:98px;width:389px;height:203px;background:#555}
.hero-photo{left:0;top:0;width:289px;height:203px;background:linear-gradient(100deg,#3d3d3d 0%,#6a6a6a 45%,#c9b8a8 60%,#777 80%,#3a3a3a 100%)}
.hero-caption{left:10px;top:16px;width:96px;height:116px;background:rgba(40,40,40,.85);padding:14px 11px;color:#fff}
.hero-caption h2{font-size:9.5px;font-weight:600;line-height:1.2;text-transform:uppercase}
.hero-caption p{font-size:6px;color:#bdbdbd;line-height:1.45;margin-top:7px}
.hero-caption a{display:block;font-size:5.6px;font-weight:700;margin-top:9px}
.hero-arrows{left:8px;top:182px;display:flex;gap:2px}
.hero-arrows span{width:13px;height:15px;background:rgba(255,255,255,.25);color:#fff;font-size:8px;text-align:center;line-height:14px}
.case-links{left:289px;top:0;width:100px;height:203px;background:var(--panel);list-style:none}
.case-links li{height:25px;border-bottom:1px solid #e6e6e6;display:flex;align-items:center;font-size:6.5px;color:#666;padding-left:8px;gap:9px}
.case-links li::before{content:"›";width:8px;height:8px;border:1px solid #ccc;border-radius:50%;font-size:7px;line-height:6px;text-align:center;color:#888}
.case-links .bar{left:0;bottom:0;width:100px;height:3px;background:#999}

.section-title{font-size:21px;font-weight:300;color:var(--ink);text-transform:uppercase;letter-spacing:.3px}
.block-title{font-size:15px;font-weight:300;color:var(--ink);text-transform:uppercase}
.sub-title{font-size:11px;font-weight:400;color:var(--ink);text-transform:uppercase}
.rule{height:1px;background:var(--rule);left:198px;width:389px}
.body-copy{font-size:5.9px;line-height:1.55;color:var(--text)}
.more{font-size:5px;font-weight:600;color:var(--ink);text-transform:uppercase}
.more::after{content:" ›"}

.services{left:198px;top:324px}
.service{top:358px;width:124px}
.service .photo{width:124px;height:72px;margin-top:10px;background:linear-gradient(135deg,#dfe3e8,#a9b0b8)}
.service .tag{font-size:5px;color:var(--orange);text-transform:uppercase;margin-top:10px}
.service .body-copy{margin-top:3px}
.service .more{display:block;margin-top:7px}

.cases-title{left:198px;top:556px}
.case-list{left:198px;top:586px;width:90px;list-style:none}
.case-list li{height:26px;border-bottom:1px solid #e2e2e2;display:flex;align-items:center;gap:8px;font-size:6.5px;font-weight:700;color:var(--ink);text-transform:uppercase}
.case-list li::before{content:"›";width:9px;height:9px;border:1px solid #ccc;border-radius:50%;font-size:7px;line-height:7px;text-align:center;color:#888;font-weight:400}
.view-all{left:198px;top:720px}
.latest-title{left:330px;top:560px}
.latest{left:330px;width:257px;display:flex;gap:8px}
.latest .photo{width:76px;height:49px;flex:none;background:linear-gradient(135deg,#d9cfc3,#8f8a86)}
.latest h4{font-size:6px;font-weight:600;color:var(--ink);text-transform:uppercase;margin:0 0 2px}
.latest .more{display:block;margin-top:3px}

.testi-title{left:198px;top:760px}
.testimonial{left:198px;width:92px}
.testimonial h4{font-size:6.5px;font-weight:600;color:var(--ink);text-transform:uppercase;margin-bottom:3px}
.testimonial .body-copy{font-size:5.5px;line-height:1.5}
.testimonial .more{display:block;text-align:right;border-bottom:1px solid #ddd;padding-bottom:2px;margin-top:2px}
.news-title{left:328px;top:764px}
.news{left:328px;top:788px;width:259px}
.news .lead{font-style:italic;color:#444;font-size:6.1px;line-height:1.5;margin-bottom:10px}
.news p + p{margin-top:9px}

.quote{left:198px;top:974px;width:389px;display:flex;gap:8px}
.quote-mark{font-size:36px;line-height:28px;color:#d2d2d2;font-weight:700;font-family:Georgia,serif}
.quote p{font-size:7.5px;font-style:italic;color:#c7c7c7;text-transform:uppercase;line-height:1.45;letter-spacing:.2px}

.foot-title{font-size:8px;font-weight:400;color:var(--ink);text-transform:uppercase;top:1029px}
.team{left:198px;top:1046px;display:grid;grid-template-columns:52px 52px;gap:6px}
.team div{width:52px;height:52px;background:linear-gradient(135deg,#e9e6e2,#b9b4ae)}
.tweets{left:330px;top:1043px;font-size:6px}
.about{left:462px;top:1049px;width:125px;font-size:5.4px;line-height:1.55;color:var(--muted)}
.about p + p{margin-top:6px}
.copyright{left:198px;top:1173px;font-size:5.2px;color:var(--muted);text-transform:uppercase}
.base-bar{left:198px;top:1194px;width:389px;height:4px;background:#222}
.to-top{left:628px;top:1150px;width:27px;height:27px;background:var(--panel);border:1px solid #ddd;font-size:5.5px;font-weight:700;color:var(--ink);display:flex;align-items:center;justify-content:center}
</style>
</head>
<body>

<nav class="main-nav abs">
  <a class="current" href="#">Home</a><a href="#">Services</a><a href="#">Case Studies</a><a href="#">Engaging Us</a><a href="#">About Conflict &amp; Low Performance</a><a href="#">Conflict Resolution App</a><a href="#">About</a><a href="#">Contact</a>
</nav>

<header>
  <div class="brand abs"><span class="brand-mark"></span><span class="brand-name">KAVILORA PARTNERS</span></div>
  <div class="brand-url abs">www.kavilora.com.au</div>
  <div class="social abs" aria-label="Social links"><span></span><span></span><span></span><span></span></div>
  <div class="brand-rule abs"></div>
</header>

<section class="hero abs">
  <div class="hero-photo abs" role="img" aria-label="Businessman offering a handshake"></div>
  <div class="hero-caption abs">
    <h2>We find the best solutions</h2>
    <p>Vivamus commodo augue et laoreet euismod, sem sapien tempor dolor lorem ip...</p>
    <a href="#">Read more ›</a>
  </div>
  <div class="hero-arrows abs"><span>‹</span><span>›</span></div>
  <ul class="case-links abs">
    <li>CASES</li><li>CASES</li><li>CASES</li><li>CASES</li><li>CASES</li><li>CASES</li><li>CASES</li><li>CASES</li>
    <span class="bar abs"></span>
  </ul>
</section>

<h2 class="section-title services abs">Our Services</h2>
<div class="rule abs" style="top:349px"></div>

<article class="service abs" style="left:198px">
  <h3 class="sub-title">Assess</h3>
  <div class="photo" role="img" aria-label="Smiling businesswoman with glasses"></div>
  <div class="tag">Lorem ipsum dolore</div>
  <p class="body-copy">At vero eos et accusamus et iusto odgnissimos ducimus qui biapraesentum voluptatu deleniti atque modestias excepturi sintot occaecati cupiditate non providenism.</p>
  <a class="more" href="#">Read more</a>
</article>
<article class="service abs" style="left:330px">
  <h3 class="sub-title">Resolve</h3>
  <div class="photo" role="img" aria-label="Bearded businessman in a suit"></div>
  <div class="tag">Massa as laoreetum</div>
  <p class="body-copy">At vero eos et accusamus et iusto odgnissimos ducimus qui biapraesentum voluptatu deleniti atque modestias excepturi sintot occaecati cupiditate non providenism.</p>
  <a class="more" href="#">Read more</a>
</article>
<article class="service abs" style="left:462px">
  <h3 class="sub-title">Develop</h3>
  <div class="photo" role="img" aria-label="Young man in a casual shirt"></div>
  <div class="tag">Nodelbat atque provident</div>
  <p class="body-copy">At vero eos et accusamus et iusto odgnissimos ducimus qui biapraesentum voluptatu deleniti atque modestias excepturi sintot occaecati cupiditate non providenism.</p>
  <a class="more" href="#">Read more</a>
</article>

<div class="rule abs" style="top:546px"></div>

<h2 class="section-title cases-title abs">Cases</h2>
<ul class="case-list abs">
  <li>Molestias</li><li>Molestias</li><li>Molestias</li><li>Molestias</li><li>Molestias</li>
</ul>
<a class="more view-all abs" href="#">View all</a>

<h3 class="block-title latest-title abs" style="font-size:12px">Latest Cases</h3>
<article class="latest abs" style="top:587px">
  <div class="photo" role="img" aria-label="Businessman smiling at his desk"></div>
  <div>
    <h4>Lorem ipsum dolore ast</h4>
    <p class="body-copy">Aprovi denslm lique sunt in culpaqui officia deserunt mollitia animi, id est laborum et dolorum fuga. Lorem ipsum dolor sit amet, consectetur adipiscing elit, sed do eiusmod tempor.</p>
    <a class="more" href="#">Read more</a>
  </div>
</article>
<article class="latest abs" style="top:664px">
  <div class="photo" role="img" aria-label="Businessman looking upward"></div>
  <div>
    <h4>Massa as laoreetum mode</h4>
    <p class="body-copy">Aprovi denslm lique sunt in culpaqui officia deserunt mollitia animi, id est laborum et dolorum fuga. Lorem ipsum dolor sit amet, consectetur adipiscing elit, sed do eiusmod tempor.</p>
    <a class="more" href="#">Read more</a>
  </div>
</article>

<div class="rule abs" style="top:744px"></div>

<h2 class="block-title testi-title abs">Testimonials</h2>
<div class="testimonial abs" style="top:792px">
  <h4>Testimonial</h4>
  <p class="body-copy">Aprovi denslm lique sunt in cul paqui officia deserunt mollitianim.</p>
  <a class="more" href="#">Continue reading</a>
</div>
<div class="testimonial abs" style="top:841px">
  <h4>Testimonial</h4>
  <p class="body-copy">Aprovi denslm lique sunt in cul paqui officia deserunt mollitianim.</p>
  <a class="more" href="#">Continue reading</a>
</div>
<div class="testimonial abs" style="top:890px">
  <h4>Testimonial</h4>
  <p class="body-copy">Aprovi denslm lique sunt in cul paqui officia deserunt mollitianim.</p>
  <a class="more" href="#">Continue reading</a>
</div>

<h2 class="block-title news-title abs" style="font-size:12px">News</h2>
<div class="news abs">
  <p class="lead">At vero eos et accusamus et iusto odgnissimos ducimus qui biapraesentum voluptatm deleniti atque modestias excepturi sintor occaecati cupiditate non.</p>
  <p class="body-copy">Aprovi denslm lique sunt in culpaqui officia deserunt mollitia animi, id est laborum et dolorum fuga. Lorem ipsum dolor sit amet, consectetur adipiscing elit, sed do eiusmod tempor incididunt ut labore massa alum. Et dolore magna aliqua. Ut enim ad minim veniam, quis nostrud exercitation ullamco laboris nisi ut aliquip ex ea commodo consequat. Duis aute irure dolor in reprehenderit in voluptate velit esse cillum dolore eu fugiat. Ipsum dolor sit amet, consectetur adipiscing elit, sed do eiusmod tempor incididunt ut labore massa adum.</p>
  <p class="body-copy">Aprovi denslm lique sunt in culpaqui officia deserunt mollitia animi, id est laborum et dolorum fuga. Lorem ipsum dolor sit amet, consectetur adipiscing elit, sed do eiusmod tempor incididunt ut labore massa alum. Et dolore magna aliqua. Ut enim ad minim veniam, quis nostrud exercitation ullamco laboris nisi ut aliquip ex ea commodo consequat. Duis aute irure dolor in reprehenderit in voluptate velit esse cillum dolore eu fugiat. Ipsum dolor sit amet, consectetur adipiscing elit, sed do eiusmod tempor incididunt ut labore massa adum.</p>
</div>

<div class="rule abs" style="top:960px"></div>
<blockquote class="quote abs">
  <span class="quote-mark">“</span>
  <p>Lorem ipsum dolor sit amet, consectetur adipiscing elit, sed do eiusmod tempor incidi dunt utlabore et dolore magna aliqua. Ut enim ad minim veniam quis nostrud.</p>
</blockquote>
<div class="rule abs" style="top:1010px"></div>

<footer>
  <h3 class="foot-title abs" style="left:198px">Our Team</h3>
  <div class="team abs">
    <div role="img" aria-label="Team member portrait"></div>
    <div role="img" aria-label="Team member portrait"></div>
    <div role="img" aria-label="Team member portrait"></div>
    <div role="img" aria-label="Team member portrait"></div>
  </div>
  <h3 class="foot-title abs" style="left:330px">Twitter</h3>
  <p class="tweets abs">loading tweets...</p>
  <h3 class="foot-title abs" style="left:462px">About Us</h3>
  <div class="about abs">
    <p>At vero eos et accusamus et iusto odio dignissimos ducimus qui blanditiis praesentium voluptatum deleniti atque.</p>
    <p>Emipit opes dolores et quas molestias excepturi sint occaecati cupiditate non provident, similique sunt in culpa qui officia deserunt.</p>
    <p>1420 Harwick Lane,<br>Brennow, DC 28 Fr 28.<br>Freephone: +1 800 604 2193</p>
  </div>
  <p class="copyright abs">© 2012 | Privacy Policy</p>
  <div class="base-bar abs"></div>
</footer>

<a class="to-top abs" href="#">TO TOP</a>

</body>
</html>
```